Lantern Bridge To Renewal social media campaign

Lantern Bridge To Renewal is a nonprofit organization that assists drug & alcohol dependent people with finding their path to longterm recovery. We are a new nonprofit and we need get the word out. Currently we have zero social media exposure and are really trying to breakout. We have a website & logo already that we would like to utilize them. Check it out lanternbridgetorenewal.example

Target Market(s)

The recovery community, people seeking help for themselves or a loved one who is addicted to drugs & alchol.

Industry/Entity Type

Drug

Colors

Designer to choose colors to be used in the design.

Requirements
Must have
• Must intergrate our brand (logo & website), inspirational and motivational theme.
Nice to have
• Go crazy let me see your ideas
Should not have
• No drug paraphernalia or anything ethicaly insenative to this epidemic.

```html
<!DOCTYPE html>
<html lang="en">
<head>
<meta charset="utf-8">
<title>Lantern Bridge To Renewal — Social Cover</title>
<link rel="stylesheet" href="https://fonts.googleapis.com/css2?family=Cormorant+Garamond:wght@500&display=swap">
<style>
  :root {
    --page: #ffffff;
    --glow-gold: #f1bf78;
    --glow-peach: #f7d9ae;
    --glow-cream: #fdf3e4;
    --stone-aqua: #a9d8d2;
    --stone-mist: #dcefeb;
    --skin-light: #f0c6a8;
    --skin-warm: #e2a583;
    --url-teal: #86c2be;
    --brand-grey: #7d8789;
    --brand-dot: #a9d6d1;
    --frame-line: #d6d6d6;
  }
  * { margin: 0; padding: 0; box-sizing: border-box; }
  html, body {
    width: 1200px;
    height: 900px;
    overflow: hidden;
    background: var(--page);
  }
  .canvas {
    position: relative;
    width: 1200px;
    height: 900px;
    background: var(--page);
  }
  .cover-banner {
    position: absolute;
    left: 84px;
    top: 260px;
    width: 1036px;
    height: 380px;
    overflow: hidden;
    background:
      radial-gradient(circle at 34% 14%, rgba(255,255,255,0.85) 0 50px, transparent 120px),
      radial-gradient(circle at 52% 34%, rgba(255,255,255,0.75) 0 45px, transparent 115px),
      radial-gradient(circle at 90% 62%, rgba(255,255,255,0.7) 0 55px, transparent 130px),
      radial-gradient(ellipse at 8% 30%, var(--glow-gold), transparent 45%),
      radial-gradient(ellipse at 62% 8%, var(--glow-gold), transparent 40%),
      radial-gradient(ellipse at 98% 18%, var(--glow-gold), transparent 45%),
      linear-gradient(100deg, var(--glow-peach) 0%, var(--glow-cream) 45%, var(--glow-peach) 100%);
  }
  .stepping-path {
    position: absolute;
    left: 30px;
    top: -10px;
    width: 520px;
    height: 400px;
    border-radius: 50% 40% 45% 50%;
    background: linear-gradient(160deg,
      rgba(169,216,210,0.75) 0%,
      rgba(220,239,235,0.85) 35%,
      rgba(169,216,210,0.7) 65%,
      rgba(220,239,235,0.35) 100%);
    clip-path: polygon(8% 0, 30% 0, 48% 40%, 95% 82%, 100% 100%, 40% 100%, 18% 60%, 2% 20%);
  }
  .helping-hand-above {
    position: absolute;
    left: 746px;
    top: -20px;
    width: 130px;
    height: 250px;
    border-radius: 40% 40% 45% 45%;
    background: radial-gradient(ellipse at 50% 40%, var(--skin-light), rgba(240,198,168,0.85) 60%, rgba(240,198,168,0) 100%);
  }
  .helping-hand-below {
    position: absolute;
    left: 636px;
    top: 160px;
    width: 140px;
    height: 240px;
    border-radius: 45% 45% 35% 35%;
    background: radial-gradient(ellipse at 50% 55%, var(--skin-warm), rgba(226,165,131,0.85) 60%, rgba(226,165,131,0) 100%);
  }
  .site-address {
    position: absolute;
    left: 260px;
    top: 140px;
    font-family: "Cormorant Garamond", serif;
    font-weight: 500;
    font-size: 31px;
    letter-spacing: 0.4px;
    color: var(--url-teal);
    white-space: nowrap;
  }
  .brand-tile {
    position: absolute;
    left: 112px;
    top: 480px;
    width: 190px;
    height: 192px;
    background: var(--page);
    border: 2px solid var(--frame-line);
    display: flex;
    flex-direction: column;
    align-items: center;
    justify-content: flex-end;
    gap: 16px;
    padding: 0 8px 22px;
  }
  .brand-dot {
    width: 44px;
    height: 44px;
    border-radius: 50%;
    background: var(--brand-dot);
  }
  .brand-name {
    font-family: "Cormorant Garamond", serif;
    font-weight: 500;
    font-size: 26px;
    line-height: 1.05;
    text-align: center;
    color: var(--brand-grey);
    white-space: nowrap;
  }
</style>
</head>
<body>
  <main class="canvas">
    <section class="cover-banner" role="img" aria-label="Soft golden bokeh light backdrop">
      <div class="stepping-path" role="img" aria-label="Pale aqua stepping stones winding up through the light"></div>
      <div class="helping-hand-above" role="img" aria-label="A hand reaching down to offer help"></div>
      <div class="helping-hand-below" role="img" aria-label="A hand reaching up to accept help"></div>
      <p class="site-address">lanternbridgetorenewal.example</p>
    </section>
    <aside class="brand-tile">
      <span class="brand-dot"></span>
      <span class="brand-name">Lantern Bridge<br>To Renewal</span>
    </aside>
  </main>
</body>
</html>
```